Glow in the Dark Inks Sales Flyer - Targeted to the music industry

We need help!
We need a creative flyer to tell the music industry about our new, colorful glow in the dark inks that look amazing on T-shirts and concert merchandise.

The flyer will go to merchandising managers for bands around the world. The design needs to be hip and contemporary but not offensive. No f-bombs please! Size is 4” x 6” or 3” x 5”, and will be printed on card stock. Design can be both sides if you want. We expect color but black and white with some fluorescent accents could be cool. Surprise us.
Here’s some copy, and we can fill in the contact info when the design is close to final.

Help your fans get lit with branded T-shirts and merchandise that glows in the dark!

Let our new Starwell Inks light up your next show!

Call us now –
Updates

Hello Designers.

Please keep in mind that although the thought of glow-in-the-dark may trigger a glowing, green color in your creative minds, StarWell Inks has a wide variety of colors to bring to offer. So please be sure to show that it's not only green glow we are promoting but we have a wide range of colors that glow (including pink, purple, white that glow blue, blue, green, orange, yellow, etc.)

Thank you!

```html
<!DOCTYPE html>
<html lang="en">
<head>
<meta charset="utf-8">
<title>Glow in the Dark Inks Flyer</title>
<link rel="stylesheet" href="https://fonts.googleapis.com/css2?family=Alegreya+Sans+SC:wght@800;900&family=Bangers&display=swap">
<style>
  :root {
    --bg: #151515;
    --bg-line: #1f1f1f;
    --bg-line-dark: #0d0d0d;
    --headline: #f2f2f2;
    --headline-shade: #b9b9b9;
    --lit-core: #ffe27a;
    --lit-edge: #ff9a1f;
    --lit-glow: rgba(255, 140, 20, 0.75);
    --glow-green: #c8ff2e;
    --glow-orange: #ffb21e;
    --glow-pink: #ff2fa8;
    --glow-cyan: #4fe6ff;
  }
  html, body {
    margin: 0;
    padding: 0;
    width: 800px;
    height: 1200px;
    overflow: hidden;
    background: var(--bg);
  }
  .flyer {
    position: relative;
    width: 800px;
    height: 1200px;
    overflow: hidden;
    background:
      repeating-linear-gradient(180deg, var(--bg-line) 0 2px, var(--bg-line-dark) 2px 5px, var(--bg) 5px 8px),
      var(--bg);
    font-family: "Alegreya Sans SC", "Arial Black", sans-serif;
    text-align: center;
    color: var(--headline);
  }
  .flyer__streak {
    position: absolute;
    left: 0;
    top: 0;
    width: 800px;
    height: 1200px;
  }
  .line {
    position: absolute;
    left: 0;
    width: 800px;
    margin: 0;
    font-weight: 900;
    line-height: 1;
    background: linear-gradient(180deg, var(--headline) 30%, var(--headline-shade) 100%);
    -webkit-background-clip: text;
    background-clip: text;
    color: transparent;
    filter: drop-shadow(0 0 6px rgba(255,255,255,0.25));
  }
  .line--help { top: 92px; font-size: 84px; letter-spacing: 2px; }
  .line--get { top: 186px; font-size: 70px; letter-spacing: 2px; }
  .line--with { top: 396px; font-size: 58px; letter-spacing: 1px; }
  .line--shirts { top: 458px; font-size: 82px; letter-spacing: 1px; }
  .line--merch { top: 540px; font-size: 80px; letter-spacing: 1px; }
  .line--that { top: 624px; font-size: 58px; letter-spacing: 1px; }
  .lit {
    position: absolute;
    left: 0;
    top: 252px;
    width: 800px;
    margin: 0;
    font-family: "Alegreya Sans SC", "Arial Black", sans-serif;
    font-weight: 900;
    font-size: 150px;
    line-height: 1;
    letter-spacing: 4px;
    color: var(--lit-core);
    background: linear-gradient(180deg, var(--lit-core) 10%, var(--lit-edge) 85%);
    -webkit-background-clip: text;
    background-clip: text;
    -webkit-text-fill-color: transparent;
    filter: drop-shadow(0 0 14px var(--lit-glow)) drop-shadow(0 0 30px var(--lit-glow));
  }
  .glow-tagline {
    position: absolute;
    left: 10px;
    top: 700px;
    width: 790px;
    margin: 0;
    font-family: "Bangers", "Comic Sans MS", cursive;
    font-weight: 400;
    font-size: 84px;
    letter-spacing: 3px;
    line-height: 1;
    transform: rotate(-8deg);
    transform-origin: center;
    white-space: nowrap;
  }
  .glow-tagline span { display: inline-block; }
  .glow--green { color: var(--glow-green); text-shadow: 0 0 10px var(--glow-green), 0 0 24px rgba(200,255,46,0.6); }
  .glow--orange { color: var(--glow-orange); text-shadow: 0 0 10px var(--glow-orange), 0 0 24px rgba(255,178,30,0.6); }
  .glow--pink { color: var(--glow-pink); text-shadow: 0 0 10px var(--glow-pink), 0 0 24px rgba(255,47,168,0.6); }
  .glow--cyan { color: var(--glow-cyan); text-shadow: 0 0 10px var(--glow-cyan), 0 0 24px rgba(79,230,255,0.6); }
</style>
</head>
<body>
  <main class="flyer">
    <svg class="flyer__streak" viewBox="0 0 800 1200" aria-hidden="true">
      <line x1="560" y1="1200" x2="800" y2="1030" stroke="rgba(255,255,255,0.12)" stroke-width="2"/>
    </svg>
    <h1 class="line line--help">Help your fans</h1>
    <p class="line line--get">get</p>
    <p class="lit">LIT</p>
    <p class="line line--with">with branded</p>
    <p class="line line--shirts">T-shirts &amp;</p>
    <p class="line line--merch">merchandise</p>
    <p class="line line--that">that</p>
    <p class="glow-tagline">
      <span class="glow--green">GLOWS</span>
      <span class="glow--orange">IN</span>
      <span class="glow--pink">THE</span>
      <span class="glow--cyan">DARK!</span>
    </p>
  </main>
</body>
</html>
```